Medical Device Packaging Project 1 of 5

We are a medical device startup company needing packaging for a total of 5 device brands. This is posting 1 of 5 and the device name is "Vexomira"

Vexomira is an intraocular lens for use in cataract surgery. The target market is Chinese ophthalmologists. The box should be sophisticated and upmarket.

The company name is Tambrel Vision, I have included the logo in the uploaded files section. You should include the logo on the box.

I have uploaded a sample lens boxes from other companies that demonstrate the information needed to be contained on the box in terms of address, warnings, symbols, etc.

I have also uploaded the blank dieline of the boxes

You are welcome and encouraged to also submit to projects 2, 3, 4, and 5 as well. The same rules and expectations apply.

Industry/Entity Type

It Company

Requirements
Should not have
• Should not have any images of an eye or any bionic/futuristic feel to the design
• Note that the quindaret box is for text reference only. You may use the lens image but the futuristic/bionic look is NOT what we are going for with this brand. It should be traditional upmarket medical device artwork.

```html
<!DOCTYPE html>
<html lang="en">
<head>
<meta charset="utf-8">
<title>Vexomira carton dieline</title>
<link rel="stylesheet" href="https://fonts.googleapis.com/css2?family=Arimo:wght@400;700&family=Oswald:wght@500&family=Montserrat:wght@500&display=swap">
<style>
  :root{
    --paper:#ffffff;
    --navy:#0e6895;
    --deep:#0d5f89;
    --flap:#289bc3;
    --sky-1:#9fd2e6;
    --sky-2:#4fa6c8;
    --white:#ffffff;
    --dim:#333333;
  }
  *{box-sizing:border-box;margin:0;padding:0}
  html,body{width:1065px;height:1200px;overflow:hidden;background:var(--paper)}
  .sheet{position:relative;width:1065px;height:1200px;font-family:"Arimo",Arial,sans-serif;color:var(--white)}
  .dieline{position:absolute;inset:0}
  .abs{position:absolute}
  .dim{position:absolute;color:var(--dim);font-family:"Times New Roman",serif;font-size:15px;white-space:nowrap}
  .dim.v{transform:rotate(-90deg);transform-origin:center}
  .wordmark{font-family:"Montserrat",Arial,sans-serif;font-weight:500;color:var(--white);letter-spacing:3px;text-align:center;white-space:nowrap;display:flex;align-items:center;gap:8px;justify-content:center}
  .wordmark .dot{width:10px;height:10px;border-radius:50%;background:var(--white);flex:none}
  .lens-art{position:absolute;border-radius:50%;background:radial-gradient(circle at 45% 40%,#eef3f6 0%,#cfdde5 60%,#a9bfcb 100%)}
  .contact{left:495px;top:140px;width:290px;font-size:10.5px;line-height:12px;font-weight:700;transform:rotate(180deg);color:#e9f3f8}
  .product{font-family:"Oswald",Arial,sans-serif;font-weight:500;letter-spacing:1px;color:var(--white)}
  .tagline{left:481px;top:538px;width:122px;font-size:11px;line-height:11px;text-align:center;border-top:1px solid var(--white);border-bottom:1px solid var(--white);padding:2px 0 1px}
  .tagline b{font-weight:700}
  .edge-claim{left:290px;top:605px;font-size:14px;font-weight:700;letter-spacing:.2px}
  .back-card{left:317px;top:757px;width:461px;height:325px;background:var(--deep)}
  .divider{left:545px;top:770px;width:1px;height:310px;background:#8cc3dc}
  .languages{left:564px;top:766px;width:210px;font-size:8.6px;line-height:8.8px;color:#e8f2f7}
  .languages p{margin-bottom:7px}
  .symbols{display:flex;align-items:center;gap:10px}
  .sterile{display:flex;border:1px solid var(--white);font-size:6px;font-weight:700;height:14px;line-height:12px}
  .sterile span{padding:0 2px}
  .sterile span+span{border-left:1px solid var(--white)}
</style>
</head>
<body>
<main class="sheet">
  <svg class="dieline" width="1065" height="1200" viewBox="0 0 1065 1200" aria-hidden="true">
    <defs>
      <radialGradient id="bokeh" cx="50%" cy="40%" r="75%">
        <stop offset="0" stop-color="#b7dff0"/>
        <stop offset=".55" stop-color="#6fb8d6"/>
        <stop offset="1" stop-color="#2c89b4"/>
      </radialGradient>
      <linearGradient id="tab" x1="0" y1="0" x2="0" y2="1">
        <stop offset="0" stop-color="#2b8dba"/>
        <stop offset="1" stop-color="#1b7aa7"/>
      </linearGradient>
    </defs>
    <!-- dust flaps -->
    <polygon fill="var(--flap)" points="148,90 272,65 272,210 262,193 148,193"/>
    <polygon fill="var(--flap)" points="808,65 932,90 932,193 818,193 808,210"/>
    <polygon fill="var(--flap)" points="148,600 260,600 272,588 272,730 148,705"/>
    <polygon fill="var(--flap)" points="808,588 820,600 932,600 932,705 808,730"/>
    <!-- glue / side tabs -->
    <path fill="var(--flap)" d="M77 210 H127 V585 H77 A25 25 0 0 1 52 560 V235 A25 25 0 0 1 77 210Z"/>
    <path fill="var(--flap)" d="M953 210 H1003 A25 25 0 0 1 1028 235 V560 A25 25 0 0 1 1003 585 H953Z"/>
    <!-- main panels -->
    <rect x="272" y="65" width="536" height="145" fill="var(--navy)"/>
    <rect x="127" y="210" width="145" height="375" fill="var(--navy)"/>
    <rect x="272" y="210" width="146" height="375" fill="url(#bokeh)"/>
    <rect x="418" y="210" width="246" height="375" fill="var(--navy)"/>
    <rect x="664" y="210" width="144" height="375" fill="url(#bokeh)"/>
    <rect x="808" y="210" width="145" height="375" fill="var(--navy)"/>
    <rect x="272" y="585" width="536" height="145" fill="var(--navy)"/>
    <rect x="272" y="730" width="536" height="378" fill="url(#bokeh)"/>
    <polygon fill="url(#tab)" points="272,1108 808,1108 804,1158 276,1158"/>
  </svg>

  <!-- dimensions -->
  <span class="dim" style="left:195px;top:33px">35mm</span>
  <span class="dim" style="left:497px;top:39px">128mm</span>
  <span class="dim" style="left:848px;top:33px">35mm</span>
  <span class="dim" style="left:68px;top:174px">18mm</span>
  <span class="dim" style="left:970px;top:174px">18mm</span>
  <span class="dim v" style="left:101px;top:126px">35mm</span>
  <span class="dim v" style="left:13px;top:381px">90mm</span>
  <span class="dim v" style="left:101px;top:631px">35mm</span>
  <span class="dim v" style="left:211px;top:921px">90mm</span>
  <span class="dim v" style="left:213px;top:1127px">12mm</span>

  <!-- top lid -->
  <div class="abs contact">
    <p>Here we would write your contact info etc</p>
    <p>which I do not know for now</p>
    <p>website: www. qxqx. com &nbsp; email: mnmn@qxi.com</p>
  </div>

  <!-- front panel -->
  <div class="abs wordmark" style="left:418px;top:268px;width:246px;font-size:21px"><span class="dot"></span>TAMBREL VISION</div>
  <div class="lens-art" role="img" aria-label="Intraocular lens with two curved haptics" style="left:468px;top:358px;width:142px;height:112px"></div>
  <div class="abs product" style="left:481px;top:503px;font-size:21px">VEXOMIRA</div>
  <div class="abs tagline"><b>Intraocular lens</b> for use<br>in cataract surgery</div>

  <!-- right side panel -->
  <div class="abs wordmark" style="left:771px;top:476px;width:220px;font-size:19px;transform:rotate(-90deg)"><span class="dot"></span>TAMBREL VISION</div>
  <svg class="abs" style="left:910px;top:222px" width="26" height="162" viewBox="0 0 26 162" aria-label="Regulatory symbols" role="img">
    <g fill="none" stroke="#fff" stroke-width="1.2">
      <circle cx="13" cy="11" r="7"/><line x1="8" y1="6" x2="18" y2="16"/>
      <circle cx="13" cy="40" r="7"/><line x1="8" y1="35" x2="18" y2="45"/>
      <circle cx="13" cy="69" r="7"/><text x="10" y="73" fill="#fff" stroke="none" font-size="10" font-family="Arimo">2</text>
      <polygon points="5,107 21,99 21,115"/>
      <rect x="6" y="122" width="14" height="38"/><line x1="6" y1="148" x2="20" y2="148"/>
    </g>
  </svg>

  <!-- bottom lid -->
  <div class="abs edge-claim">WITH 360° SQUARE EDGE</div>
  <div class="abs wordmark" style="left:418px;top:647px;width:246px;font-size:21px"><span class="dot"></span>TAMBREL VISION</div>

  <!-- back panel -->
  <div class="abs back-card"></div>
  <div class="abs product" style="left:360px;top:762px;font-size:25px">VEXOMIRA</div>
  <div class="lens-art" role="img" aria-label="Intraocular lens with two curved haptics" style="left:368px;top:878px;width:132px;height:150px"></div>
  <div class="abs divider"></div>
  <div class="abs languages">
    <p>Contains one sterile intraocular lens<br>Do not use if the packaging is damaged<br>Do not resterilize</p>
    <p>Bevat één steriele intraoculaire lens<br>Niet gebruiken als de verpakking beschadigd is<br>Niet opnieuw steriliseren</p>
    <p>Contient une lentille intraoculaire stérile<br>Ne pas utiliser si l'emballage est endommagé<br>Ne pas restériliser</p>
    <p>Enthält eine sterile intraokulare Linse<br>Nicht verwenden, wenn die Verpackung beschädigt ist<br>Nicht resterilisieren</p>
    <p>Periéchei éna aposteiroméno endofthálmia fakó OR<br>Περιέχει ένα αποστειρωμένο ενδοφθάλμια φακό<br>Μην το χρησιμοποιείτε εάν η συσκευασία έχει υποστεί ζημιά<br>OR Min to chrisimopoieíte eán i syskevasía échei ypostei zimiá<br>Μην επαναποστειρώνετε &nbsp;OR Min epanaposteirónete</p>
    <p>Contiene una lente intraoculare sterile<br>Non usare se la confezione è danneggiata<br>Non risterilizzare</p>
    <p>Contém uma lente intra-ocular esterilizada<br>Não use se a embalagem está danificada<br>Não reesterilize</p>
    <p>Contiene una lente intraocular estéril<br>No utilizar si el envase está dañado<br>No vuelva a esterilizar</p>
    <div class="symbols">
      <div class="sterile"><span>STERILE</span><span>EO</span></div>
      <svg width="124" height="18" viewBox="0 0 124 18" role="img" aria-label="Warning and single-use symbols">
        <g fill="none" stroke="#fff" stroke-width="1.2">
          <polygon points="9,2 17,16 1,16"/><line x1="9" y1="7" x2="9" y2="12"/>
          <circle cx="41" cy="9" r="7.5"/><text x="38" y="13" fill="#fff" stroke="none" font-size="10" font-family="Arimo">2</text>
          <circle cx="73" cy="9" r="7.5"/><line x1="68" y1="4" x2="78" y2="14"/>
          <circle cx="105" cy="9" r="7.5"/><line x1="100" y1="4" x2="110" y2="14"/>
        </g>
      </svg>
    </div>
  </div>
</main>
</body>
</html>
```